Web site for small printshop

I am looking for a website for small printshop in Iceland, mainly serving university students and artist.

We print posters, flyers, business cards and more.

In addition to our current website, I would like to include design tool, (fx. www.quarlitune.example, www.dravonpix.example or something similar) jobs upload, shopping chart.
Updates

Great work, I am really amazed of the quality of work i am seeing here.

Really way beyond my expectation

GOOD JOB - all of you ! 

Hi all.

The designs submitted have been great, way better than expected.
I really did not expect this level of quality.

Some have been asking me for feedback on their designs, and I will try 
to send some feedback here, without spoiling your creativity.

Likes:
- when the colors of my logo is used in menus, buttons etc.
- simple, not to crowded look.

Dislikes.
- Dark and heavy design
- Lot of text and buttons (crowded look)

Extra info.
- top line (before menus) will contain: Tel - email - language
- menu line will have 5 categories: Home - service - submission of works - FAQ - about us
- 3 large buttons:  Job submit - Job design - ask for offer

LOVE YOUR WORK - great designs so far :)

Target Market(s)

University Students, Artists. Age group 20-30

Industry/Entity Type

University

Requirements
Must have
• The website must be easy to use, clean looking.

```html
<!DOCTYPE html>
<html lang="en">
<head>
<meta charset="utf-8">
<title>Vellirprent – Print Shop</title>
<link href="https://fonts.googleapis.com/css2?family=Open+Sans:wght@400;600;700;800&display=swap" rel="stylesheet">
<style>
:root{
  --green:#1b7a3c;
  --green-dark:#125c2c;
  --ink:#2b2b2b;
  --muted:#8a8a8a;
  --topbar:#1e1e1e;
  --light:#efefef;
  --slate:#4b4f58;
  --yellow:#f2cf1d;
  --footer:#1d1d1d;
  --bottom:#3d3a3a;
  --white:#ffffff;
}
*{margin:0;padding:0;box-sizing:border-box}
html,body{width:1200px;height:3214px;overflow:hidden}
body{font-family:"Open Sans",Arial,sans-serif;color:var(--ink);background:var(--white);position:relative}
.abs{position:absolute}
section,header,footer,.topbar{position:absolute;left:0;width:1200px}

/* top bar */
.topbar{top:0;height:64px;background:var(--topbar);color:#ddd;font-size:12px;font-weight:600;white-space:nowrap}
.topbar .contact{left:96px;top:24px;display:flex;gap:36px}
.topbar .contact span{display:flex;align-items:center;gap:12px}
.topbar .account{right:90px;top:24px;display:flex;gap:18px;align-items:center}
.dot-icon{width:16px;height:16px;border-radius:50%;background:#ddd;display:inline-block}

/* header */
.site-header{top:64px;height:130px;background:var(--white)}
.brand{left:126px;top:36px;display:flex;align-items:center;gap:14px;font-size:34px;font-weight:800;color:var(--ink);letter-spacing:1px}
.brand-mark{width:40px;height:40px;background:var(--green)}
.main-nav{right:120px;top:54px;display:flex;gap:44px;font-size:17px;font-weight:700;color:#3a3a3a}
.main-nav .active{color:var(--green)}

/* hero */
.hero{top:194px;height:476px;background:linear-gradient(90deg,#6e7072,#8b8e8f 40%,#a3a5a4)}
.hero-photo{left:0;top:0;width:1200px;height:476px;background:radial-gradient(ellipse at 48% 45%,#b57a55 0 18%,#7d4b3c 30%,transparent 55%)}
.hero-dots{left:560px;top:438px;display:flex;gap:10px}
.hero-dots i{width:12px;height:12px;border-radius:50%;background:#ddd;display:block}
.hero-dots i.on{background:var(--green)}

/* actions */
.actions{top:670px;height:320px;background:var(--white)}
.action{width:240px;text-align:center;top:68px}
.action .circle{width:96px;height:96px;margin:0 auto;border-radius:50%;background:var(--green);display:flex;align-items:center;justify-content:center;box-shadow:inset 0 -10px 0 var(--green-dark)}
.action h3{margin-top:34px;font-size:20px;font-weight:800}
.action p{margin-top:16px;font-size:12px;line-height:16px;color:var(--muted)}
.connector{top:115px;height:0;border-top:3px dashed #cfcfcf;width:130px}

/* who we are */
.who{top:990px;height:395px;background:var(--light)}
.who-photo{left:236px;top:56px;width:409px;height:275px;background:linear-gradient(180deg,#d9dadb,#9fa3a6)}
.who h2{left:702px;top:56px;font-size:26px;font-weight:800}
.who p{left:702px;top:104px;width:360px;font-size:13px;line-height:19px;color:var(--muted)}
.who-thumb{top:183px;width:112px;height:97px;background:linear-gradient(180deg,#b9a58f,#4e4540)}
.who-more{left:702px;top:308px;display:flex;align-items:center;gap:14px;font-size:13px;color:var(--muted)}

.arrow-btn{width:22px;height:22px;background:var(--green);display:inline-flex;align-items:center;justify-content:center}

/* templates */
.templates{top:1385px;height:476px;background:var(--white)}
.section-title{width:1200px;text-align:center;font-size:30px;font-weight:800;left:0}
.templates .lead{left:220px;top:104px;width:760px;text-align:center;font-size:15px;line-height:24px;color:#555}
.filters{left:236px;top:178px;display:flex;gap:20px;font-size:13px;color:#555;align-items:center}
.filters .sep{width:1px;height:16px;background:#ccc}
.filters .pager{display:flex;gap:4px;margin-left:4px}
.tpl{top:222px;width:166px;height:153px}
.tpl-cap{top:396px;display:flex;align-items:center;gap:34px;font-size:13px;color:#555}

/* benefits */
.benefits{top:1861px;height:394px;background:var(--slate);color:var(--white)}
.benefits .section-title{top:56px;color:var(--white)}
.benefits .lead{left:0;width:1200px;top:112px;text-align:center;font-size:15px;color:#d6d6d6}
.benefit{width:200px;display:flex;gap:12px}
.benefit .num{flex:none;width:30px;height:30px;background:var(--white);color:var(--ink);font-weight:800;font-size:18px;display:flex;align-items:center;justify-content:center}
.benefit h4{font-size:13px;font-weight:800;margin-top:2px}
.benefit p{font-size:11px;line-height:15px;color:#cfd0d3;margin-top:6px}

/* team */
.team{top:2255px;height:412px;background:#f3f3f3}
.team .section-title{top:52px}
.member{top:107px;width:180px;text-align:center}
.member .photo{width:180px;height:163px;background:linear-gradient(180deg,#d4d4d4,#3e3e42)}
.member h4{margin-top:22px;font-size:17px;font-weight:800;color:var(--green)}
.member p{margin-top:6px;font-size:11px;line-height:15px;color:var(--muted)}
.socials{margin-top:14px;display:flex;gap:6px;justify-content:center}
.socials i{width:18px;height:18px;background:#c9c9c9;display:block}

/* testimonial */
.testimonial{top:2667px;height:212px;background:var(--yellow)}
.testimonial .section-title{top:20px;font-weight:700;color:#3a3a3a}
.quote-mark{font-size:90px;font-weight:800;color:#6a5b12;line-height:1}
.testimonial blockquote{left:360px;top:80px;width:500px;text-align:center;font-size:15px;line-height:22px;color:#4a4212}
.author{left:540px;top:150px;display:flex;align-items:center;gap:14px;font-size:10px;color:#4a4212}
.author strong{display:block;font-size:11px}
.author .avatar{width:44px;height:44px;background:linear-gradient(#c9b29a,#5b4a40);border:2px solid var(--white)}

/* footer */
.site-footer{top:2879px;height:236px;background:var(--footer);color:#cfcfcf}
.f-col h5{font-size:15px;font-weight:800;color:var(--white);margin-bottom:18px}
.f-col p{font-size:12px;line-height:20px}
.f-more{margin-top:16px;display:flex;align-items:center;gap:14px;font-size:12px}
.gallery{display:grid;grid-template-columns:80px 80px;gap:10px}
.gallery i{display:block;height:44px;background:linear-gradient(135deg,#7a5a45,#2f3a44)}
.tweet{width:240px;height:44px;background:#333;margin-bottom:12px;display:flex;align-items:center;gap:10px;padding:0 10px;font-size:10px}
.tweet .badge{margin-left:auto;width:50px;height:34px;background:#4a4a4a;text-align:center;font-size:10px;padding-top:4px}
.tw-nav{right:210px;top:28px;display:flex;gap:6px}
.tw-nav i{width:22px;height:22px;background:#eee;display:flex;align-items:center;justify-content:center}

.bottombar{top:3115px;height:99px;background:var(--bottom);color:#ccc;font-size:11px;white-space:nowrap}
.bottombar .copy{left:177px;top:42px}
.bottombar .links{left:464px;top:42px;display:flex;gap:8px}
.bottombar .links span+span::before{content:"|";margin-right:8px;color:#777}
.bottombar .social{left:858px;top:38px;display:flex;gap:12px}
.bottombar .social i{width:20px;height:20px;background:#eee;display:block}
</style>
</head>
<body>

<div class="topbar">
  <div class="abs contact"><span><i class="dot-icon"></i>+354 555 0142</span><span><i class="dot-icon"></i>info@vellirprent.example</span></div>
  <div class="abs account"><span>WELCOME MSG!</span><span>My Account</span><span>My Cart</span><span>Checkout</span><span>$ 0.00</span><span>language ▾</span><span>USD ▾</span>
    <svg width="16" height="16" viewBox="0 0 18 18"><circle cx="7" cy="7" r="5.5" fill="none" stroke="#ddd" stroke-width="2"/><path d="M11 11l5 5" stroke="#ddd" stroke-width="2.4"/></svg>
  </div>
</div>

<header class="site-header">
  <div class="abs brand"><span class="brand-mark"></span>VELLIRPRENT</div>
  <nav class="abs main-nav"><span class="active">Home</span><span>Service</span><span>Submission of Works</span><span>FAQs</span><span>Contact us</span></nav>
</header>

<section class="hero">
  <div class="abs hero-photo" role="img" aria-label="Smiling student leaning on a stack of books in front of a chalkboard"></div>
  <div class="abs hero-dots"><i></i><i></i><i class="on"></i><i></i><i></i></div>
</section>

<section class="actions">
  <div class="abs connector" style="left:390px"></div>
  <div class="abs connector" style="left:665px"></div>
  <div class="abs action" style="left:201px">
    <div class="circle"><svg width="50" height="50" viewBox="0 0 50 50"><circle cx="25" cy="25" r="21" fill="none" stroke="#fff" stroke-width="4"/><path d="M25 14v22M14 25h22" stroke="#fff" stroke-width="5"/></svg></div>
    <h3>JOB SUBMIT</h3><p>Send your files for print today and<br>we will check them within the hour<br>and prepare a proof for you fast</p>
  </div>
  <div class="abs action" style="left:475px">
    <div class="circle"><svg width="50" height="50" viewBox="0 0 50 50"><circle cx="25" cy="25" r="21" fill="none" stroke="#fff" stroke-width="4"/><path d="M16 34l3-9 12-12 6 6-12 12z" fill="#fff"/></svg></div>
    <h3>JOB DESIGN</h3><p>Build your poster or card online<br>with our simple design tool and<br>order prints straight from the page</p>
  </div>
  <div class="abs action" style="left:750px">
    <div class="circle"><svg width="50" height="50" viewBox="0 0 50 50"><circle cx="25" cy="25" r="21" fill="none" stroke="#fff" stroke-width="4"/><path d="M25 14a11 9 0 1 1-6 17l-6 3 3-6a11 9 0 0 1 9-14z" fill="#fff"/></svg></div>
    <h3>ASK FOR OFFER</h3><p>Tell us about your print job and<br>get a fair price offer by email<br>for large runs and special paper</p>
  </div>
</section>

<section class="who">
  <div class="abs who-photo" role="img" aria-label="Portrait of a young man in a white shirt"></div>
  <h2 class="abs">WHO WE ARE</h2>
  <p class="abs">Small print shop in the heart of town serving students and artists with posters, flyers and cards.</p>
  <div class="abs who-thumb" style="left:702px" role="img" aria-label="Team member photo"></div>
  <div class="abs who-thumb" style="left:833px" role="img" aria-label="Team member photo"></div>
  <div class="abs who-thumb" style="left:964px" role="img" aria-label="Team member photo"></div>
  <div class="abs who-more">Read more about us <span class="arrow-btn"><svg width="10" height="10" viewBox="0 0 10 10"><path d="M2 1l6 4-6 4z" fill="#fff"/></svg></span></div>
</section>

<section class="templates">
  <h2 class="abs section-title" style="top:52px">OUR POPULAR TEMPLATES</h2>
  <p class="abs lead">Pick a ready made layout for posters, flyers and business cards, change the text and colours, then send it straight to print with one click.</p>
  <div class="abs filters"><span>Posters all</span><i class="sep"></i><span>Flyers and cards</span><i class="sep"></i><span>Event posters</span><i class="sep"></i><span>Brochures</span><i class="sep"></i><span>Student projects</span><i class="sep"></i><span>Art</span>
    <span class="pager"><span class="arrow-btn"><svg width="10" height="10" viewBox="0 0 10 10"><path d="M8 1L2 5l6 4z" fill="#fff"/></svg></span><span class="arrow-btn"><svg width="10" height="10" viewBox="0 0 10 10"><path d="M2 1l6 4-6 4z" fill="#fff"/></svg></span></span>
  </div>
  <div class="abs tpl" style="left:241px;background:linear-gradient(160deg,#b76a52,#5a3a4a)" role="img" aria-label="Template preview: building facade"></div>
  <div class="abs tpl" style="left:418px;background:linear-gradient(180deg,#2f3e52,#8c5a45)" role="img" aria-label="Template preview: rocket launch"></div>
  <div class="abs tpl" style="left:595px;background:linear-gradient(180deg,#e7c48a,#5d8a64)" role="img" aria-label="Template preview: landscape with trees"></div>
  <div class="abs tpl" style="left:772px;background:linear-gradient(180deg,#d9c8a5,#8a6a55)" role="img" aria-label="Template preview: house drawing"></div>
  <div class="abs tpl-cap" style="left:254px">Open layout <span class="arrow-btn"><svg width="10" height="10" viewBox="0 0 10 10"><path d="M2 1l6 4-6 4z" fill="#fff"/></svg></span></div>
  <div class="abs tpl-cap" style="left:431px">Open layout <span class="arrow-btn"><svg width="10" height="10" viewBox="0 0 10 10"><path d="M2 1l6 4-6 4z" fill="#fff"/></svg></span></div>
  <div class="abs tpl-cap" style="left:608px">Open layout <span class="arrow-btn"><svg width="10" height="10" viewBox="0 0 10 10"><path d="M2 1l6 4-6 4z" fill="#fff"/></svg></span></div>
  <div class="abs tpl-cap" style="left:785px">Open layout <span class="arrow-btn"><svg width="10" height="10" viewBox="0 0 10 10"><path d="M2 1l6 4-6 4z" fill="#fff"/></svg></span></div>
</section>

<section class="benefits">
  <h2 class="abs section-title">WHAT YOU CAN GET FROM HERE</h2>
  <p class="abs lead">Good prints at student prices with friendly help from our small team</p>
  <div class="abs benefit" style="left:182px;top:178px"><span class="num">1</span><div><h4>LOW PRICE</h4><p>Fair prices for students<br>and artists on every job</p></div></div>
  <div class="abs benefit" style="left:396px;top:178px"><span class="num">2</span><div><h4>SPECIAL OFFER</h4><p>Monthly deals on posters<br>flyers and business cards</p></div></div>
  <div class="abs benefit" style="left:611px;top:178px"><span class="num">3</span><div><h4>HIGHT QUALITY</h4><p>Sharp colour on quality<br>paper for every print run</p></div></div>
  <div class="abs benefit" style="left:825px;top:178px"><span class="num">4</span><div><h4>FREE DELIVERY SERVICE</h4><p>Free delivery to campus<br>for all orders over limit</p></div></div>
  <div class="abs benefit" style="left:182px;top:258px"><span class="num">5</span><div><h4>FREE TEMPLATES</h4><p>Ready layouts for every<br>kind of print you need</p></div></div>
  <div class="abs benefit" style="left:396px;top:258px"><span class="num">6</span><div><h4>DESIGN BY YOU</h4><p>Make your own design in<br>our simple online editor</p></div></div>
  <div class="abs benefit" style="left:611px;top:258px"><span class="num">7</span><div><h4>EASY TOOL</h4><p>Upload, preview and pay<br>in just a few short steps</p></div></div>
  <div class="abs benefit" style="left:825px;top:258px"><span class="num">8</span><div><h4>CUSTOMER SUPPORT</h4><p>Ask us anything by phone<br>or email during the week</p></div></div>
</section>

<section class="team">
  <h2 class="abs section-title">OUR CUSTOMER SERVICE</h2>
  <div class="abs member" style="left:222px"><div class="photo" role="img" aria-label="Staff portrait"></div><h4>TÓMAS VIDAR</h4><p>Print and file support<br>weekdays from nine</p><div class="socials"><i></i><i></i><i></i><i></i><i></i></div></div>
  <div class="abs member" style="left:420px"><div class="photo" role="img" aria-label="Staff portrait"></div><h4>TÓMAS VIDAR</h4><p>Print and file support<br>weekdays from nine</p><div class="socials"><i></i><i></i><i></i><i></i><i></i></div></div>
  <div class="abs member" style="left:618px"><div class="photo" role="img" aria-label="Staff portrait"></div><h4>TÓMAS VIDAR</h4><p>Print and file support<br>weekdays from nine</p><div class="socials"><i></i><i></i><i></i><i></i><i></i></div></div>
  <div class="abs member" style="left:816px"><div class="photo" role="img" aria-label="Staff portrait"></div><h4>TÓMAS VIDAR</h4><p>Print and file support<br>weekdays from nine</p><div class="socials"><i></i><i></i><i></i><i></i><i></i></div></div>
</section>

<section class="testimonial">
  <h2 class="abs section-title">WHAT THEY SAY</h2>
  <span class="abs quote-mark" style="left:290px;top:62px">“</span>
  <blockquote class="abs">Fast, friendly and my posters looked great on the wall. I order my exhibition prints here and always get them on time.</blockquote>
  <span class="abs quote-mark" style="left:880px;top:78px">”</span>
  <div class="abs author"><div><strong>ANNA LIND</strong>Art Student</div><span class="avatar" role="img" aria-label="Customer photo"></span></div>
</section>

<footer class="site-footer">
  <div class="abs f-col" style="left:177px;top:50px"><h5>WHO WE ARE</h5><p>Small print shop for<br>students and artists,<br>posters, flyers, cards<br>and more every day</p><div class="f-more">Read More <span class="arrow-btn"><svg width="10" height="10" viewBox="0 0 10 10"><path d="M2 1l6 4-6 4z" fill="#fff"/></svg></span></div></div>
  <div class="abs f-col" style="left:396px;top:50px"><h5>ADRESS</h5><p>12 Lindargata<br>Reykjavík 101<br>Hours M-F 8:00am-5:00pm<br>Fax: 354 555 0178</p><div class="f-more"><svg width="14" height="18" viewBox="0 0 14 18"><path d="M7 0a7 7 0 0 1 7 7c0 5-7 11-7 11S0 12 0 7a7 7 0 0 1 7-7z" fill="#ddd"/><circle cx="7" cy="7" r="2.5" fill="#1d1d1d"/></svg>Open in map</div></div>
  <div class="abs f-col" style="left:573px;top:50px"><h5>PRINT GALLERY</h5><div class="gallery" role="img" aria-label="Gallery of printed works"><i></i><i></i><i></i><i></i></div></div>
  <div class="abs f-col" style="left:782px;top:50px"><h5>TWEETS</h5>
    <div class="tweet"><span>new poster sizes now in stock</span><span class="badge">2<br>days ago</span></div>
    <div class="tweet"><span>free delivery to campus this week</span><span class="badge">2<br>days ago</span></div>
  </div>
  <div class="abs tw-nav"><i><svg width="10" height="10" viewBox="0 0 10 10"><path d="M8 1L2 5l6 4z" fill="#1d1d1d"/></svg></i><i><svg width="10" height="10" viewBox="0 0 10 10"><path d="M2 1l6 4-6 4z" fill="#1d1d1d"/></svg></i></div>
</footer>

<div class="abs bottombar" style="left:0;width:1200px">
  <div class="abs copy">© 2013 Your Company. All Rights Reserved.</div>
  <div class="abs links"><span>about us</span><span>lates news</span><span>privacy policy</span><span>FAQs</span><span>contact us</span></div>
  <div class="abs social"><i></i><i></i><i></i><i></i><i></i></div>
</div>

</body>
</html>
```